Business Card design for amazing new Dental Office

Please read this brief closely!

Our client is a modern new dental office/
They love their new logo.
Now it's time to create a business card for them.

It should be a two sided card:
Side one should have the logo and name and maybe a color background or design.
Side two should have all the contact information which is here:

Marcus Holloway, D.D.S
General and Cosmetic Dentistry
4187 W. Pinecrest Avenue
Ventura, CA 93011
(805) 912-4386
drmarcus@bluefernsmiles-example.com
www.bluefernsmiles-example.com

Feel free to arrange that info as you like and to style both sides of the card according to your creativity. This is a chance for you to show your design skills!

Client is open to font choices and is looking for a style that is amazing and premium. Colors can be selected from the logo, or any variation of those.

You will not win this contest with a less than beautiful card design so please feel free to make multiple submissions.

Logo files attached and please message me with any questions.
Thanks!

Target Market(s)

Families and Professionals seeking dental services

Industry/Entity Type

Dental

Contact Information for Business Card

Logo, style, contact info as per the brief

Font styles to use
Sans Serif

Requirements
Must have
• Client's logo and contact details as per brief
Nice to have
• Unique style reflecting high end dental clinic near the beach
Should not have
• Must not look like a template

```html
<!DOCTYPE html>
<html lang="en">
<head>
<meta charset="utf-8">
<title>Blue Fern Smiles – Business Card</title>
<link rel="stylesheet" href="https://fonts.googleapis.com/css2?family=Lato:wght@300;400&display=swap">
<style>
  :root {
    --page-bg: #eef0f1;
    --card-white: #ffffff;
    --sky-blue: #4db3e6;
    --sky-blue-light: #7cc8ef;
    --sand: #e0a456;
    --ink-grey: #5e6163;
    --brand-grey: #8d9093;
  }
  html, body {
    margin: 0;
    width: 1200px;
    height: 1200px;
    overflow: hidden;
    background: var(--page-bg);
    font-family: "Lato", sans-serif;
  }
  .card {
    position: absolute;
    left: 222px;
    width: 754px;
    height: 463px;
    overflow: hidden;
  }
  .card--front { top: 105px; background: var(--card-white); }
  .card--back  { top: 630px; background: var(--sky-blue); }

  .brand {
    position: absolute;
    margin: 0;
    font-weight: 300;
    letter-spacing: 0.08em;
    text-transform: uppercase;
    white-space: nowrap;
    display: flex;
    align-items: center;
    gap: 14px;
  }
  .brand__dot {
    display: inline-block;
    width: 14px;
    height: 14px;
    border-radius: 50%;
    background: currentColor;
  }
  .card--front .brand {
    right: 46px;
    top: 160px;
    font-size: 34px;
    color: var(--brand-grey);
  }

  .doctor {
    position: absolute;
    left: 46px;
    top: 218px;
  }
  .doctor__name {
    margin: 0;
    font-size: 32px;
    font-weight: 400;
    color: var(--sky-blue);
    line-height: 1.1;
  }
  .doctor__role {
    margin: 4px 0 0;
    font-size: 19px;
    font-weight: 400;
    color: var(--ink-grey);
  }
  .divider {
    position: absolute;
    left: 46px;
    right: 46px;
    top: 299px;
    height: 2px;
    background: var(--sand);
  }

  .contact-list {
    position: absolute;
    left: 46px;
    top: 326px;
    margin: 0;
    padding: 0;
    list-style: none;
  }
  .contact-list li {
    display: flex;
    align-items: center;
    height: 31px;
    font-size: 21px;
    font-weight: 300;
    color: var(--ink-grey);
  }
  .contact-list svg { width: 22px; height: 22px; margin-right: 14px; flex: none; }

  .address {
    position: absolute;
    right: 46px;
    top: 334px;
    text-align: right;
    font-size: 21px;
    font-weight: 300;
    color: var(--ink-grey);
    line-height: 27px;
    font-style: normal;
  }
  .address__pin { display: block; margin: 0 0 6px auto; width: 18px; height: 26px; }

  .edge-bands { position: absolute; left: 0; bottom: 0; width: 754px; height: 16px; }

  .back-wash {
    position: absolute;
    inset: 0;
    background:
      radial-gradient(circle at 22% 25%, rgba(124,200,239,0.55) 0, rgba(124,200,239,0) 45%),
      radial-gradient(circle at 88% 55%, rgba(124,200,239,0.35) 0, rgba(124,200,239,0) 40%),
      var(--sky-blue);
  }
  .card--back .brand {
    left: 0;
    right: 0;
    justify-content: center;
    top: 230px;
    font-size: 44px;
    color: var(--card-white);
  }
</style>
</head>
<body>

<section class="card card--front" aria-label="Business card front">
  <p class="brand"><span class="brand__dot"></span>Blue Fern Smiles</p>

  <div class="doctor">
    <h1 class="doctor__name">Marcus Holloway, D.D.S</h1>
    <p class="doctor__role">General and Cosmetic Dentistry</p>
  </div>

  <div class="divider"></div>

  <ul class="contact-list">
    <li>
      <svg viewBox="0 0 24 24" aria-hidden="true"><path fill="#4db3e6" d="M6.6 10.8a15.2 15.2 0 0 0 6.6 6.6l2.2-2.2a1 1 0 0 1 1-.25 11.4 11.4 0 0 0 3.6.57 1 1 0 0 1 1 1V20a1 1 0 0 1-1 1A17 17 0 0 1 3 4a1 1 0 0 1 1-1h3.5a1 1 0 0 1 1 1c0 1.25.2 2.45.57 3.57a1 1 0 0 1-.25 1z"/></svg>
      (805) 912-4386
    </li>
    <li>
      <svg viewBox="0 0 24 24" aria-hidden="true"><rect x="1" y="4" width="18" height="13" rx="1" fill="#4db3e6"/><path d="M1.5 5l8.5 6.5L18.5 5" fill="none" stroke="#fff" stroke-width="1.5"/><circle cx="18" cy="17" r="5" fill="#4db3e6" stroke="#fff" stroke-width="1.5"/><path d="M15.6 17l1.7 1.7 3-3" fill="none" stroke="#fff" stroke-width="1.5"/></svg>
      drmarcus@bluefernsmiles-example.com
    </li>
    <li>
      <svg viewBox="0 0 24 24" aria-hidden="true"><g fill="none" stroke="#4db3e6" stroke-width="1.5"><circle cx="12" cy="12" r="10"/><ellipse cx="12" cy="12" rx="4.5" ry="10"/><path d="M2 12h20M4 6.5h16M4 17.5h16"/></g></svg>
      www.bluefernsmiles-example.com
    </li>
  </ul>

  <address class="address">
    <svg class="address__pin" viewBox="0 0 18 26" aria-hidden="true"><path fill="#4db3e6" d="M9 0a9 9 0 0 1 9 9c0 6.5-9 17-9 17S0 15.5 0 9a9 9 0 0 1 9-9z"/><circle cx="9" cy="9" r="3.2" fill="#fff"/></svg>
    4187 W. Pinecrest Avenue<br>
    Ventura, CA 93011
  </address>

  <svg class="edge-bands" viewBox="0 0 754 16" preserveAspectRatio="none" aria-hidden="true">
    <polygon points="0,0 444,0 440,16 0,16" fill="#4db3e6"/>
    <polygon points="450,0 754,0 754,16 446,16" fill="#e0a456"/>
  </svg>
</section>

<section class="card card--back" aria-label="Business card back">
  <div class="back-wash" role="img" aria-label="Soft light-blue wave shapes across the blue background"></div>
  <p class="brand"><span class="brand__dot"></span>Blue Fern Smiles</p>
</section>

</body>
</html>
```